Website visual upgrade

I am seeking expressions of interest for the updating the visuals of my website www.lunvaleplacements.example
I am basically seeking a simple,bold and visually strong graphic makeover.using existing or shortly to be modified text.

```html
<!DOCTYPE html>
<html lang="en">
<head>
<meta charset="utf-8">
<title>Lunvale Placements</title>
<link rel="stylesheet" href="https://fonts.googleapis.com/css2?family=Roboto:wght@300;400;500;700&display=swap">
<style>
:root{
  --red:#c0122f;
  --ink:#333333;
  --text:#555555;
  --nav:#353535;
  --card:#f2f2f2;
  --line:#dddddd;
  --footer:#4b4b4b;
  --blue:#1a6fc4;
}
*{margin:0;padding:0;box-sizing:border-box}
html,body{width:960px;height:1200px;overflow:hidden;background:#fff}
body{font-family:'Roboto',sans-serif;color:var(--text);position:relative}
.abs{position:absolute}
.top-band{left:0;top:0;width:960px;height:118px;background:linear-gradient(#e4e4e4,#f0f0f0)}
.brand{left:104px;top:40px;display:flex;align-items:center;gap:10px}
.brand-mark{width:22px;height:22px;border-radius:50%;background:var(--red)}
.brand-name{font-size:28px;font-weight:500;color:var(--red);letter-spacing:.5px}
.contact{left:696px;top:36px}
.contact-row{display:flex;align-items:center;gap:10px}
.phone{font-size:20px;color:var(--red);letter-spacing:.5px}
.email{font-size:11px;color:var(--blue);margin-top:4px}
.hero{left:0;top:118px;width:960px;height:408px;background:linear-gradient(100deg,#6b6558 0%,#9a958a 35%,#b7b3aa 60%,#8c6a4c 85%,#6d5e50 100%)}
.nav{left:105px;top:102px;width:752px;height:35px;background:var(--nav);display:flex;align-items:center;justify-content:space-around;padding:0 6px;border-radius:2px}
.nav a{color:#fff;text-decoration:none;font-size:9.6px;letter-spacing:.3px}
.cap-title{left:552px;top:253px;width:304px;height:42px;background:rgba(30,30,30,.85);color:#fff;font-size:22px;line-height:42px;text-align:right;padding-right:12px;letter-spacing:.5px}
.cap-text{left:409px;top:299px;width:447px;height:61px;background:rgba(255,255,255,.88);color:var(--red);font-size:14.5px;line-height:21px;text-align:right;padding:11px 12px 0 0}
.dots{left:780px;top:487px;display:flex;gap:4px}
.dots span{width:16px;height:16px;border-radius:50%;background:rgba(255,255,255,.75)}
.dots span:first-child{background:#fff}
h2{font-weight:400;text-transform:uppercase;color:var(--ink);letter-spacing:.5px}
h2 em{font-style:normal;color:var(--red)}
.who{left:0;top:546px;width:960px;text-align:center}
.who h2{font-size:19px}
.who p{width:720px;margin:6px auto 0;font-size:10.4px;line-height:20px;color:var(--text)}
.card{top:661px;width:240px;height:264px;background:var(--card);border:1px solid #e2e2e2;box-shadow:0 1px 2px rgba(0,0,0,.15);padding:14px 15px 0}
.card h2{font-size:16px}
.card .photo{width:210px;height:94px;margin-top:10px;border-radius:3px;border:1px solid #ccc}
.card p{font-size:9.6px;line-height:16px;text-align:center;margin-top:8px;height:80px}
.btn{display:block;width:71px;height:21px;margin:0 auto;background:#4a4a4a;color:#fff;font-size:10.4px;line-height:21px;text-align:center;border-radius:2px}
.supports{left:104px;top:942px;width:752px;height:130px;background:var(--card);border:1px solid #e2e2e2;box-shadow:0 1px 2px rgba(0,0,0,.15)}
.supports h2{text-align:center;font-size:16px;margin-top:12px}
.sup{top:38px;width:357px;height:82px;background:#fff;border:1px solid var(--line);border-radius:3px;display:flex;align-items:center;padding:0 10px}
.sup .badge{flex:none;display:flex;align-items:center;justify-content:center;font-size:11px;font-weight:500}
.sup p{font-size:9.4px;line-height:16px;color:var(--text)}
.footer{left:0;top:1088px;width:960px;height:112px;background:var(--footer);color:#e6e6e6}
.flinks{left:104px;top:22px;font-size:11px;word-spacing:2px}
.flinks span{margin:0 12px;color:#ccc}
.copy{left:104px;top:60px;font-size:9.6px;line-height:19px;color:#cfcfcf}
.copy b{color:#fff;font-weight:500}
.connect{left:740px;top:18px;font-size:12px;color:#fff}
.social{left:741px;top:49px;display:flex;gap:6px}
.social span{width:24px;height:24px;border-radius:3px}
</style>
</head>
<body>
<div class="abs top-band"></div>
<div class="abs hero" role="img" aria-label="Construction worker in hard hat and high-visibility vest on a building site with an excavator"></div>

<div class="abs brand"><span class="brand-mark"></span><span class="brand-name">Lunvale Placements</span></div>

<div class="abs contact">
  <div class="contact-row">
    <svg width="16" height="12" viewBox="0 0 16 12"><path d="M1 4c4-4 10-4 14 0l-2 2-2-1V3H5v2L3 6z M3 7h10v5H3z" fill="#666"/></svg>
    <span class="phone">61-3-95550142</span>
  </div>
  <div class="contact-row">
    <svg width="16" height="10" viewBox="0 0 16 10"><rect x=".5" y=".5" width="15" height="9" fill="none" stroke="#777"/><path d="M.5 .5l7.5 5 7.5-5" fill="none" stroke="#777"/></svg>
    <span class="email">admin@lunvaleplacements.example</span>
  </div>
</div>

<nav class="abs nav">
  <a>HOME</a><a>WHO WE ARE</a><a>OUR APPROACH</a><a>WHAT WE DO</a><a>MIGRATION ASSISTANCE</a><a>JOB SEEKERS</a><a>USEFUL LINKS</a><a>SUPPORT</a><a>CONTACT US</a>
</nav>

<div class="abs cap-title">Lorem ipsum dolor sit amet</div>
<div class="abs cap-text">Vestibulum vel metus sit amet turpis bibendum tincidunt vel<br>sit amet quam.lobortis turpis in odio blandit ac interdum</div>
<div class="abs dots"><span></span><span></span><span></span><span></span></div>

<section class="abs who">
  <h2><em>Who</em> we are</h2>
  <p>We are committed to providing the highest standards of service in Executive search and selection and the provision of Skilled trades people and allied Health professionals throughout Australia. We have offices throughout Australia, clearly adding value to our clients’ strategic needs, wherever they may be.</p>
</section>

<article class="abs card" style="left:104px">
  <h2><em>What</em> we do</h2>
  <div class="photo" role="img" aria-label="Group of smiling healthcare professionals" style="background:linear-gradient(90deg,#d9d4cf,#a9a29a 50%,#6f8f4a)"></div>
  <p>We are a specialist recruiter to the Health sector. Our clienes andts are primarily engaged in the management of acute hospitals, residential aged care facilities community care service..</p>
  <span class="btn">Read More</span>
</article>

<article class="abs card" style="left:360px">
  <h2><em>Our</em> approach</h2>
  <div class="photo" role="img" aria-label="Business people shaking hands in a meeting" style="background:linear-gradient(90deg,#3e4c66,#8c96a8 50%,#4a5368)"></div>
  <p>We think laterally about our clients’ needs and deliver a “fresh approach” to Executive search and selection and the provision of Skilled trades people and allied Health recruitment.</p>
  <span class="btn">Read More</span>
</article>

<article class="abs card" style="left:616px">
  <h2><em>Migration</em> assistance</h2>
  <div class="photo" role="img" aria-label="Family standing in front of a recruitment office sign" style="background:linear-gradient(180deg,#6f7f88,#3a302c 60%,#bdb5ad)"></div>
  <p>We can provide processing assistance to employers who are seeking suitably skilled and experienced staff from overseas on an appropriate temporary/permanent business visa.</p>
  <span class="btn">Read More</span>
</article>

<section class="abs supports">
  <h2><em>Our</em> supports</h2>
  <div class="abs sup" style="left:12px">
    <div class="badge" style="width:140px;height:60px;color:var(--red)">BrightPath Youth</div>
    <p style="margin-left:18px">BrightPath’s mission is to support, develop and empower young people living with cancer.</p>
  </div>
  <div class="abs sup" style="left:383px">
    <div class="badge" style="width:60px;height:64px;background:#111"></div>
    <p style="margin-left:20px">The Kalinda Community Fund supports a range of community projects focused on young people in Africa and Australia.</p>
  </div>
</section>

<footer class="abs footer">
  <div class="abs flinks">Home<span>/</span>Contact Us<span>/</span>Privacy Policy<span>/</span>Site Map</div>
  <div class="abs copy">Copyright 2013. <b>Lunvale Placements.</b><br>All Right Reserved</div>
  <div class="abs connect">Connect Us</div>
  <div class="abs social"><span style="background:#3b5a9a"></span><span style="background:#3fa9d6"></span><span style="background:#1f74a8"></span><span style="background:#f08a1d"></span></div>
</footer>
</body>
</html>
```